Laptop Accessories Packing Design

We are looking for a new package design of a laptop accesories (batteries, charges, hard drives etc.). We want to refresh our brand Velmora GridWorks. At VelmoraGrid, we create high-end laptop accessories that ensure reliability, performance, and longevity for users worldwide. Our mission is to deliver innovative and durable solutions that allow users to work, create, and grow without limits.
General Packaging Concept
Minimalist and elegant look, yet with elements that catch the eye (Velmora products will mainly be offered on auction portals such as Trivana, Zubo, Kestrix, so it would be good if the packaging attracted attention and stood out from the competitors).
Should I put a photo, sketch or product icon on the box? We'll leave that to your imagination.
We ask for a general design of the packaging. After the competition, together with the winner, we will add the rest of the information to the back and sides of the box.
In the attachments there is our Logo (you can use other colors) and sample packaging of competitors
Target Market(s)
E-commerse
Industry/Entity Type
individual end customer
Look and feel
Each slider illustrates characteristics of the customer's brand and the style your logo design should communicate.

```html
<!DOCTYPE html>
<html lang="en">
<head>
<meta charset="utf-8">
<title>Velmora GridWorks – Laptop Battery Packaging</title>
<link rel="stylesheet" href="https://fonts.googleapis.com/css2?family=Michroma&display=swap">
<style>
  :root {
    --stage: #d9d9d9;
    --box-black: #050505;
    --box-charcoal: #161616;
    --white: #ffffff;
    --gold-light: #f6d33a;
    --gold: #d9a90f;
    --gold-deep: #8a6a05;
    --badge-blue: #3f78b8;
    --badge-blue-dark: #1d4474;
    --badge-text: #dfeaf7;
  }
  * { margin: 0; padding: 0; box-sizing: border-box; }
  html, body {
    width: 1200px;
    height: 454px;
    overflow: hidden;
    background: var(--stage);
  }
  .package-front {
    position: absolute;
    left: 0;
    top: 53px;
    width: 1200px;
    height: 348px;
    overflow: hidden;
    background: radial-gradient(ellipse at 25% 50%, var(--box-charcoal) 0%, var(--box-black) 75%);
    font-family: "Michroma", sans-serif;
  }
  .hero-art {
    position: absolute;
    right: 0;
    top: 0;
    width: 760px;
    height: 348px;
    background:
      radial-gradient(ellipse 60% 55% at 78% 48%, rgba(246, 211, 58, 0.85) 0%, rgba(217, 169, 15, 0.45) 35%, rgba(0, 0, 0, 0) 70%),
      linear-gradient(90deg, rgba(0, 0, 0, 0) 0%, rgba(138, 106, 5, 0.35) 55%, rgba(217, 169, 15, 0.55) 100%);
  }
  .light-streak {
    position: absolute;
    left: 360px;
    top: 262px;
    width: 840px;
    height: 12px;
    background: radial-gradient(ellipse 50% 50% at 60% 50%, rgba(255, 236, 150, 0.95) 0%, rgba(217, 169, 15, 0.5) 40%, rgba(0, 0, 0, 0) 100%);
  }
  .brand-name {
    position: absolute;
    left: 84px;
    top: 40px;
    font-size: 44px;
    line-height: 1;
    color: var(--white);
    letter-spacing: -1px;
  }
  .product-title {
    position: absolute;
    left: 88px;
    top: 170px;
    line-height: 1;
  }
  .product-title .line {
    display: block;
    font-size: 47px;
    letter-spacing: -1px;
  }
  .product-title .line-primary { color: var(--white); }
  .product-title .line-accent {
    margin-top: 4px;
    background: linear-gradient(180deg, var(--gold-light) 0%, var(--gold) 55%, var(--gold-deep) 100%);
    -webkit-background-clip: text;
    background-clip: text;
    color: transparent;
  }
  .range-badge {
    position: absolute;
    left: 84px;
    top: 276px;
    width: 212px;
    height: 24px;
    border-radius: 3px;
    background: linear-gradient(180deg, var(--badge-blue) 0%, var(--badge-blue-dark) 100%);
    color: var(--badge-text);
    font-size: 11.5px;
    line-height: 24px;
    text-align: center;
    letter-spacing: -0.3px;
  }
</style>
</head>
<body>
  <main class="package-front">
    <div class="hero-art" role="img" aria-label="Open laptop bathed in golden light with bursting sparks and light trails over a black hexagon-textured background"></div>
    <div class="light-streak"></div>
    <div class="brand-name">Velmora</div>
    <h1 class="product-title">
      <span class="line line-primary">LAPTOP</span>
      <span class="line line-accent">BATTERY</span>
    </h1>
    <div class="range-badge">PREMIUM ACCESSORIES</div>
  </main>
</body>
</html>
```